Analytics software company needs a business card design

We need a business card design for a global analytics software provider called 'Varnel Software'. Our main focus is developing real estate analysis software. We are open to any color scheme. The final design should be simple, modern, and precise.
Updates

There is one day left in our project and we are still looking forward to receiving additional submissions. We look forward to selecting one of your designs. Thanks.

Industry/Entity Type

Real Estate

```html
<!DOCTYPE html>
<html lang="en">
<head>
<meta charset="utf-8">
<title>Varnel Software – Business Card</title>
<link href="https://fonts.googleapis.com/css2?family=Open+Sans:wght@400;600;700&display=swap" rel="stylesheet">
<style>
  :root {
    --page: #e9e7e3;
    --card-black: #0c0d0f;
    --card-panel: #2a2b2f;
    --card-back: #1d1e21;
    --band-light: #3a3b40;
    --accent-blue: #3aa6e8;
    --accent-violet: #4b3fd6;
    --text-light: #e4e6ea;
    --text-muted: #9ea3ab;
  }
  html, body {
    margin: 0;
    width: 1200px;
    height: 1023px;
    overflow: hidden;
    background: var(--page);
    font-family: "Open Sans", Arial, sans-serif;
  }
  .canvas {
    position: relative;
    width: 1200px;
    height: 1023px;
  }
  .card {
    position: absolute;
    left: 250px;
    width: 700px;
    height: 400px;
    border-radius: 6px;
    overflow: hidden;
    box-shadow: 0 10px 30px rgba(0,0,0,0.25);
  }
  .card-front { top: 90px; background: var(--card-black); }
  .card-back  { top: 533px; background: var(--card-back); }
  .card-art {
    position: absolute;
    inset: 0;
    width: 100%;
    height: 100%;
  }
  .brand-name {
    position: absolute;
    margin: 0;
    font-weight: 600;
    color: var(--accent-blue);
    letter-spacing: 0.5px;
    white-space: nowrap;
  }
  .card-front .brand-name {
    top: 52px;
    right: 48px;
    font-size: 30px;
  }
  .brand-dot {
    display: inline-block;
    width: 12px;
    height: 12px;
    border-radius: 50%;
    background: var(--accent-blue);
    margin-right: 10px;
    vertical-align: middle;
    position: relative;
    top: -3px;
  }
  .holder {
    position: absolute;
    left: 40px;
    top: 196px;
  }
  .holder-name {
    margin: 0;
    font-size: 26px;
    font-weight: 700;
    color: var(--accent-blue);
    letter-spacing: 1px;
    text-transform: uppercase;
  }
  .holder-role {
    margin: 2px 0 0;
    font-size: 15px;
    color: var(--accent-blue);
  }
  .contact-list {
    position: absolute;
    left: 330px;
    top: 262px;
    margin: 0;
    padding: 0;
    list-style: none;
  }
  .contact-list li {
    display: flex;
    align-items: center;
    font-size: 14.5px;
    color: var(--text-light);
    height: 24px;
  }
  .contact-icon {
    width: 14px;
    height: 14px;
    margin-right: 10px;
    flex: none;
  }
  .contact-address {
    position: absolute;
    left: 330px;
    top: 350px;
    margin: 0;
    font-size: 16px;
    font-weight: 700;
    color: var(--accent-blue);
    text-transform: uppercase;
    letter-spacing: 0.3px;
  }
  .back-brand {
    position: absolute;
    left: 0;
    right: 0;
    top: 150px;
    text-align: center;
  }
  .back-brand .brand-name {
    position: static;
    font-size: 40px;
  }
  .tagline {
    margin: 14px 0 0;
    font-size: 15px;
    color: var(--text-light);
    letter-spacing: 1px;
    text-transform: uppercase;
  }
</style>
</head>
<body>
<main class="canvas">

  <section class="card card-front" aria-label="Business card front">
    <svg class="card-art" viewBox="0 0 700 400" aria-hidden="true">
      <defs>
        <linearGradient id="swoosh" x1="0" y1="1" x2="1" y2="0">
          <stop offset="0" stop-color="#3aa6e8"/>
          <stop offset="0.5" stop-color="#4b5fe0"/>
          <stop offset="1" stop-color="#4b3fd6"/>
        </linearGradient>
      </defs>
      <path d="M0,400 L0,352 C260,312 500,195 700,62 L700,400 Z" fill="#2a2b2f"/>
      <path d="M0,350 C260,310 500,193 700,60" fill="none" stroke="url(#swoosh)" stroke-width="9"/>
    </svg>

    <p class="brand-name"><span class="brand-dot"></span>Varnel Software</p>

    <div class="holder">
      <h1 class="holder-name">Marc Delowen</h1>
      <p class="holder-role">President | CEO</p>
    </div>

    <ul class="contact-list">
      <li>
        <svg class="contact-icon" viewBox="0 0 14 14" aria-hidden="true">
          <rect width="14" height="14" rx="2" fill="#9ea3ab"/>
          <path d="M4 3 L6 3 L6.5 5.5 L5.3 6.3 C5.8 7.4 6.6 8.2 7.7 8.7 L8.5 7.5 L11 8 L11 10 C7 10.5 3.5 7 4 3 Z" fill="#0c0d0f"/>
        </svg>
        805-410-7362
      </li>
      <li>
        <svg class="contact-icon" viewBox="0 0 14 14" aria-hidden="true">
          <rect width="14" height="14" rx="2" fill="#9ea3ab"/>
          <rect x="3" y="4" width="8" height="6" fill="none" stroke="#0c0d0f" stroke-width="1.2"/>
          <path d="M3 4 L7 7.5 L11 4" fill="none" stroke="#0c0d0f" stroke-width="1.2"/>
        </svg>
        mdelowen@varnelsoftware.com
      </li>
      <li>
        <svg class="contact-icon" viewBox="0 0 14 14" aria-hidden="true">
          <rect width="14" height="14" rx="2" fill="#9ea3ab"/>
          <circle cx="7" cy="7" r="4" fill="none" stroke="#0c0d0f" stroke-width="1.1"/>
          <path d="M3 7 H11 M7 3 C5 5 5 9 7 11 M7 3 C9 5 9 9 7 11" fill="none" stroke="#0c0d0f" stroke-width="1"/>
        </svg>
        www.varnelsoftware.com
      </li>
    </ul>
    <p class="contact-address">482 Harlow Lane Ventura, CA 93001</p>
  </section>

  <section class="card card-back" aria-label="Business card back">
    <svg class="card-art" viewBox="0 0 700 400" aria-hidden="true">
      <path d="M80,0 C40,140 60,280 150,400 L110,400 C20,280 0,140 40,0 Z" fill="#2c2d32"/>
      <path d="M640,0 C700,140 690,280 600,400 L560,400 C650,280 660,140 600,0 Z" fill="#3a3b40"/>
      <path d="M120,0 C90,140 110,280 190,400 L170,400 C90,280 70,140 100,0 Z" fill="#26272b"/>
    </svg>
    <div class="back-brand">
      <p class="brand-name"><span class="brand-dot"></span>Varnel Software</p>
      <p class="tagline">Global Analytics Software Provider</p>
    </div>
  </section>

</main>
</body>
</html>
```